High End Business Card Design for Flooring Store

Looking for a new card design for our hardwood flooring company. We have no print budget for these and are open to cards made from wood, metal, cardstock with embossed print ... or any combination of these. No plastic.

We sell luxury products and I want the cards to reflect our image of quality and class.

Our contact information as such;
Employee Name
418 Colbrook Blvd.
Harwick, NB
K9R-3M5
(555) 214-3968
Employee email @velkaflooring.com

Target Market(s)

Home Builders

Contact Information for Business Card

Emnployee name, business contact information

```html
<!DOCTYPE html>
<html lang="en">
<head>
<meta charset="UTF-8">
<title>Velka Flooring – Business Card</title>
<link href="https://fonts.googleapis.com/css2?family=Montserrat:wght@400;500;600&family=Poppins:wght@600&display=swap" rel="stylesheet">
<style>
  :root {
    --page: #ffffff;
    --ink: #3d3733;
    --silver-light: #f4f3f4;
    --silver-mid: #b2b0b1;
    --silver-dark: #9e9b9c;
    --edge: #6f6c6d;
    --gold-deep: #6e5217;
    --gold-bright: #e8b22c;
    --gold-warm: #a47c1e;
  }
  html, body {
    margin: 0;
    width: 1200px;
    height: 848px;
    overflow: hidden;
    background: var(--page);
  }
  .canvas {
    position: relative;
    width: 1200px;
    height: 848px;
  }
  .card {
    position: absolute;
    width: 550px;
    height: 314px;
    border-radius: 36px;
    overflow: hidden;
    color: var(--ink);
    box-sizing: border-box;
  }
  .card--back {
    left: 554px;
    top: 87px;
    border: 1px solid var(--edge);
    background: linear-gradient(125deg,
      var(--silver-light) 0%, var(--silver-mid) 12%, var(--silver-dark) 22%,
      var(--silver-mid) 45%, var(--silver-light) 62%, #ffffff 66%,
      var(--silver-mid) 80%, #77737a 100%);
  }
  .card--front {
    left: 98px;
    top: 448px;
    border: 1px solid #d9d8d9;
    background: linear-gradient(115deg,
      var(--silver-dark) 0%, #ffffff 13%, var(--silver-mid) 26%,
      var(--silver-mid) 40%, var(--silver-dark) 56%, #c9c8c9 66%,
      #ffffff 82%, #d4d3d4 92%, var(--silver-mid) 100%);
  }
  .wordmark {
    position: absolute;
    font-family: "Montserrat", sans-serif;
    font-weight: 500;
    line-height: 1;
    margin: 0;
  }
  .card--back .wordmark {
    left: 58px;
    top: 18px;
    font-size: 62px;
    letter-spacing: 1px;
  }
  .card--front .wordmark {
    left: 92px;
    width: 400px;
    text-align: center;
    top: 90px;
    font-size: 94px;
    letter-spacing: 2px;
  }
  .tagline {
    position: absolute;
    margin: 0;
    font-family: "Montserrat", sans-serif;
    font-weight: 400;
    text-align: center;
    line-height: 1.1;
  }
  .card--back .tagline {
    left: 61px;
    width: 200px;
    top: 75px;
    font-size: 14.5px;
  }
  .card--front .tagline {
    left: 92px;
    width: 400px;
    top: 176px;
    font-size: 22px;
  }
  .employee {
    position: absolute;
    left: 39px;
    top: 126px;
    margin: 0;
    font-family: "Montserrat", sans-serif;
    font-weight: 600;
    font-size: 21px;
    letter-spacing: 0.8px;
  }
  .divider {
    position: absolute;
    left: 40px;
    top: 162px;
    width: 200px;
    height: 2px;
    background: var(--ink);
  }
  .contact {
    position: absolute;
    left: 39px;
    margin: 0;
    font-family: "Poppins", sans-serif;
    font-weight: 600;
    font-size: 12.5px;
    letter-spacing: 2.6px;
    line-height: 15.7px;
  }
  .contact--address { top: 177px; }
  .contact--phone { top: 240px; }
  .contact--email { top: 271px; }
  .accent-field {
    position: absolute;
    left: 367px;
    top: 35px;
    width: 183px;
    height: 279px;
    background: linear-gradient(170deg,
      var(--gold-deep) 0%, var(--gold-bright) 45%, var(--gold-warm) 100%);
    opacity: 0.9;
  }
</style>
</head>
<body>
  <main class="canvas">
    <section class="card card--back" aria-label="Business card, contact side">
      <p class="wordmark">Velka</p>
      <p class="tagline">Parquets &amp; Finitions<br>Hardwood &amp; Trims</p>
      <h1 class="employee">Marc Lavoie</h1>
      <div class="divider"></div>
      <p class="contact contact--address">418 Colbrook Blvd.<br>Harwick, NB<br>K9R-3M5</p>
      <p class="contact contact--phone">(555) 214-3968</p>
      <p class="contact contact--email">lavoie@velkaflooring.com</p>
      <div class="accent-field" role="img" aria-label="Gold brand decoration area"></div>
    </section>

    <section class="card card--front" aria-label="Business card, brand side">
      <p class="wordmark">Velka</p>
      <p class="tagline">Parquets &amp; Finitions<br>Hardwood &amp; Trims</p>
    </section>
  </main>
</body>
</html>
```